IT Distribution Wholesale Business Card & Logo Design

I need both logo and a business card that suits our business model, am happy to pay more for great effort put in.
Brevon Orbital Australia Pty Ltd
An IT Distribution / Wholesale company that distributes technology hardwares, softwares, components, etc.
Offer drop ship services for online retailers and supply to Australia-wide.
Based in Sydney Australia.
Design should give impressions of trust and stability.

Slogan: "your one stop technology supplier"
*two-sided name card
*logo + slogan on the back of the card

I don't have much specific requirements, leave it to designers to come up with creative & interesting masterpiece.
The logo and business card comes in first which i would like it to be completed latest by mid of March, we will require a whole redesign of our web pages, banner design, catalogue design later part.

Goodluck & thank you for your effort.

Hello designers,

Busy week, very good return rate on the number of designs and effort put into our business card design.
I thank you all for that.
We will have to extend this project for another week to two to receive more designs and more time for me to post some updates to you all.
We are getting there, i really liked some of the designs sent but just not the perfect masterpiece we are looking for.

Cheers,
Darnell Q.

Target Market(s)

Computer Retailers, Corporate, Schools, Councils.

Industry/Entity Type

Business

Requirements
Must have
• Brevon Orbital (Australia) Pty Ltd, Darnell Quist, Managing Director, Unit C, 14-18 Pellham Road, Dunmore NSW 2461, Ph +61 2 5037 1942, M +61 4 70395216, E darnell@brevonorbital.com.au, W www.brevonorbital.com.au
Nice to have
• Keep it simple & comfortable.
Target audiences are mostly >30-40 years old range.

Example of companies in the same line:-
http://www.kzp.com.au
http://www.norvix.com.au/
http://www.supplyhaventrade.com/
http://www.quenby.com.au/
http://www.bq456.com.au/
https://www.swiftgridhub.com.au/
http://carvelo.com.au/

```html
<!DOCTYPE html>
<html lang="en">
<head>
<meta charset="utf-8">
<title>Darnell Quist – Business Card</title>
<link rel="stylesheet" href="https://fonts.googleapis.com/css2?family=Russo+One&family=Raleway:wght@200;300&display=swap">
<style>
  :root {
    --card-bg: #ffffff;
    --brand-blue: #0d568f;
    --brand-blue-soft: rgba(13, 86, 143, 0.16);
    --brand-blue-faint: rgba(13, 86, 143, 0.04);
    --name-dark: #3c3c3e;
    --title-grey: #5a5a5a;
    --contact-grey: #9a9a9a;
    --label-blue: #3a86c4;
  }
  html, body {
    margin: 0;
    padding: 0;
    overflow: hidden;
    background: var(--card-bg);
  }
  .card {
    position: relative;
    width: 1200px;
    height: 657px;
    background: var(--card-bg);
    overflow: hidden;
  }
  .card__emblem {
    position: absolute;
    left: 655px;
    top: -40px;
    width: 600px;
    height: 545px;
    border-radius: 50%;
    background: radial-gradient(ellipse at 55% 45%, var(--brand-blue-soft) 0%, var(--brand-blue-faint) 60%, rgba(13, 86, 143, 0) 72%);
  }
  .person__name {
    position: absolute;
    left: 18px;
    top: 72px;
    margin: 0;
    font-family: "Russo One", sans-serif;
    font-weight: 400;
    font-size: 58px;
    letter-spacing: 1px;
    line-height: 1;
  }
  .person__first { color: var(--brand-blue); }
  .person__last { color: var(--name-dark); }
  .person__title {
    position: absolute;
    left: 18px;
    top: 188px;
    margin: 0;
    font-family: "Raleway", sans-serif;
    font-weight: 200;
    font-size: 37px;
    letter-spacing: 2px;
    color: var(--title-grey);
    line-height: 1;
  }
  .contact {
    position: absolute;
    left: 18px;
    top: 478px;
    margin: 0;
    padding: 0;
    list-style: none;
    font-family: "Raleway", sans-serif;
    font-weight: 200;
    font-size: 27px;
    letter-spacing: 3px;
    font-variant-numeric: lining-nums;
    color: var(--contact-grey);
    text-transform: uppercase;
  }
  .contact__line {
    height: 34px;
    line-height: 34px;
    white-space: nowrap;
  }
  .contact__label { color: var(--label-blue); }
</style>
</head>
<body>
  <div class="card">
    <div class="card__emblem" role="img" aria-label="Company emblem: large blue orbital arc mark"></div>

    <h1 class="person__name"><span class="person__first">Darnell</span> <span class="person__last">Quist</span></h1>
    <p class="person__title">MANAGING DIRECTOR</p>

    <ul class="contact">
      <li class="contact__line">Unit C, 14-18 Pellham Road, Dunmore NSW 2461</li>
      <li class="contact__line"><span class="contact__label">PH</span> : +61 2 5037 1942</li>
      <li class="contact__line"><span class="contact__label">M</span> : +61 4 70395216</li>
      <li class="contact__line"><span class="contact__label">E</span> : darnell@brevonorbital.com.au</li>
      <li class="contact__line">www.brevonorbital.com.au</li>
    </ul>
  </div>
</body>
</html>
```